Flyer Design Project - Pebblestone Stillness

I require a flyer to be created for a course. It is a meditation course. So I want the cover design to look quirky but calm.

I have attached a previous design. This project is for Pebblestone stillness. Although I have attached the previous flyer for guidance of the lay out and words used, I DO NOT want to to be a direct copy, I want it to look completely different. SO be creative. Any copies or anything that looks close to a copy will not even be considered.

I want the flyer to be A5 side but also the ability to resize it onto smaller cards.

If you need further information about the design brief please contact me.

Target Market(s)

20 to 40 year olds

Requirements
Must have
• Must have space for a logo which is currently being designed by the artwork hive. For the time being insert the still maple grove wellness logo which is attached.

Picture something related to wine on the front and course detail on the back same as the attached sample.
Should not have
• a direct copy of my samples I have attached.

```html
<!DOCTYPE html>
<html lang="en">
<head>
<meta charset="utf-8">
<title>Pebblestone Stillness Course – Flyer, Front and Back</title>
<link rel="stylesheet" href="https://fonts.googleapis.com/css2?family=Fraunces:opsz,wght@9..144,400;9..144,700&family=Nunito+Sans:wght@400;700&display=swap">
<style>
  :root{
    --wine:#5a1f33;
    --wine-deep:#3d1322;
    --claret:#8c2f4b;
    --rose:#c9768a;
    --blush:#f2d9d6;
    --cream:#f7f0e7;
    --stone:#d8cfc4;
    --stone-dark:#b9ada0;
    --sage:#8fa58a;
    --ink:#3a2a2c;
    --white:#ffffff;
  }
  *{margin:0;padding:0;box-sizing:border-box}
  html,body{width:846px;height:1200px;overflow:hidden}
  body{font-family:"Nunito Sans",Arial,sans-serif;color:var(--ink);background:var(--cream)}
  .flyer{position:relative;width:846px;height:1200px;overflow:hidden}

  /* FRONT (cover) */
  .front{position:absolute;left:0;top:0;width:846px;height:600px;background:var(--wine);color:var(--cream)}
  .front__photo{position:absolute;left:0;top:0;width:400px;height:600px;
    background:radial-gradient(ellipse at 55% 60%,var(--claret) 0%,var(--wine-deep) 70%),var(--wine-deep);
    border-radius:0 200px 200px 0}
  .front__content{position:absolute;left:444px;top:64px;width:366px}
  .front__kicker{font-size:14px;font-weight:700;letter-spacing:3px;text-transform:uppercase;color:var(--rose)}
  .front__title{font-family:"Fraunces",Georgia,serif;font-weight:700;font-size:62px;line-height:66px;margin-top:18px;color:var(--cream)}
  .front__title em{font-style:normal;color:var(--blush)}
  .front__tagline{font-family:"Fraunces",Georgia,serif;font-size:21px;line-height:30px;margin-top:22px;color:var(--blush)}
  .pebbles{display:flex;align-items:flex-end;gap:10px;margin-top:30px}
  .pebble{display:block;border-radius:50%}
  .pebble--a{width:54px;height:34px;background:var(--stone)}
  .pebble--b{width:38px;height:26px;background:var(--stone-dark)}
  .pebble--c{width:24px;height:17px;background:var(--sage)}
  .front__brand{position:absolute;left:444px;top:500px;display:flex;align-items:center;gap:14px}
  .brand-mark{width:44px;height:44px;background:var(--cream)}
  .brand-name{font-size:15px;line-height:20px;font-weight:700;color:var(--cream)}
  .brand-name small{display:block;font-size:12px;font-weight:400;letter-spacing:1.5px;text-transform:uppercase;color:var(--rose)}

  /* BACK (course details) */
  .back{position:absolute;left:0;top:600px;width:846px;height:600px;background:var(--cream)}
  .back__col{position:absolute;top:46px}
  .back__col--left{left:48px;width:372px}
  .back__col--right{left:460px;width:340px;background:var(--blush);border-radius:24px;padding:26px 24px 24px;top:40px}
  .heading{font-family:"Fraunces",Georgia,serif;font-weight:700;color:var(--wine)}
  .heading--lg{font-size:30px;line-height:36px}
  .heading--md{font-size:22px;line-height:28px;margin-top:26px}
  .body{font-size:16px;line-height:25px;margin-top:10px}
  .accent{color:var(--claret);font-weight:700}
  .perks{list-style:none;margin-top:14px}
  .perks li{position:relative;padding-left:28px;font-size:15.5px;line-height:23px;margin-top:10px}
  .perks svg{position:absolute;left:0;top:4px;width:16px;height:16px}
  .back__strip{position:absolute;left:0;bottom:0;width:846px;height:74px;background:var(--wine);
    color:var(--cream);display:flex;align-items:center;justify-content:space-between;padding:0 48px;font-weight:700;font-size:19px}
  .contact{display:flex;align-items:center;gap:10px}
  .contact svg{width:20px;height:20px}
</style>
</head>
<body>
<main class="flyer">
  <section class="front" aria-label="Front cover">
    <div class="front__photo" role="img" aria-label="Photo of a glass of red wine on a calm, softly lit table"></div>
    <div class="front__content">
      <p class="front__kicker">A mindful wine course</p>
      <h1 class="front__title">Pebblestone <em>Stillness</em></h1>
      <p class="front__tagline">Sip slowly. Breathe deeply.<br>Notice every note.</p>
      <div class="pebbles" aria-hidden="true">
        <span class="pebble pebble--a"></span><span class="pebble pebble--b"></span><span class="pebble pebble--c"></span>
      </div>
    </div>
    <div class="front__brand">
      <span class="brand-mark" aria-hidden="true"></span>
      <span class="brand-name"><small>Brought to you by</small>Still Maple Grove Wellness</span>
    </div>
  </section>

  <section class="back" aria-label="Course details">
    <div class="back__col back__col--left">
      <h2 class="heading heading--lg">Wine what?!</h2>
      <p class="body">Yes you read right. <span class="accent">Pebblestone stillness!</span> What could be better than combining the rich taste of a good glass of wine with meditation, right? That is exactly what this course is about, with a little bit of Mindfulness poured in.</p>
      <h2 class="heading heading--md">Learn to enjoy a glass, one mindful sip at a time</h2>
      <p class="body">“What do you mean? I already know how to drink wine.” We challenge you that you have never really tasted it. We will teach you to slow down, notice every note and savour each sip mindfully.</p>
    </div>

    <div class="back__col back__col--right">
      <h2 class="heading heading--lg">What you get</h2>
      <ul class="perks">
        <li><svg viewBox="0 0 16 16" aria-hidden="true"><path d="M2 8.5l4 4 8-9" fill="none" stroke="#8c2f4b" stroke-width="2.2" stroke-linecap="round" stroke-linejoin="round"/></svg>A Pebblestone Stillness course book</li>
        <li><svg viewBox="0 0 16 16" aria-hidden="true"><path d="M2 8.5l4 4 8-9" fill="none" stroke="#8c2f4b" stroke-width="2.2" stroke-linecap="round" stroke-linejoin="round"/></svg>Mindfulness and meditation instruction online</li>
        <li><svg viewBox="0 0 16 16" aria-hidden="true"><path d="M2 8.5l4 4 8-9" fill="none" stroke="#8c2f4b" stroke-width="2.2" stroke-linecap="round" stroke-linejoin="round"/></svg>Learn how to taste wine mindfully</li>
        <li><svg viewBox="0 0 16 16" aria-hidden="true"><path d="M2 8.5l4 4 8-9" fill="none" stroke="#8c2f4b" stroke-width="2.2" stroke-linecap="round" stroke-linejoin="round"/></svg>Learn meditation techniques and postures</li>
        <li><svg viewBox="0 0 16 16" aria-hidden="true"><path d="M2 8.5l4 4 8-9" fill="none" stroke="#8c2f4b" stroke-width="2.2" stroke-linecap="round" stroke-linejoin="round"/></svg>FREE mp3 guided meditation download</li>
        <li><svg viewBox="0 0 16 16" aria-hidden="true"><path d="M2 8.5l4 4 8-9" fill="none" stroke="#8c2f4b" stroke-width="2.2" stroke-linecap="round" stroke-linejoin="round"/></svg>5% of the course goes to charity — see our website for this month’s cause</li>
      </ul>
    </div>

    <div class="back__strip">
      <span class="contact"><svg viewBox="0 0 24 24" aria-hidden="true"><path d="M6.6 10.8a15 15 0 0 0 6.6 6.6l2.2-2.2a1 1 0 0 1 1-.25 11.4 11.4 0 0 0 3.6.57 1 1 0 0 1 1 1V20a1 1 0 0 1-1 1A17 17 0 0 1 3 4a1 1 0 0 1 1-1h3.5a1 1 0 0 1 1 1c0 1.25.2 2.45.57 3.57a1 1 0 0 1-.25 1z" fill="#f7f0e7"/></svg>(02) 5550 1846</span>
      <span>www.Pebblestone-stillness.com.au</span>
    </div>
  </section>
</main>
</body>
</html>
```